Business Card Design Project

Company name will be Tolvan Crest (named after my black lab and his fraying muzzle) Business is in the body armor, Security product industry servicing the state, local, and federal law enforcement markets. I want a more formal and serious logo for both business cards and letterhead

```html
<!DOCTYPE html>
<html lang="en">
<head>
<meta charset="utf-8">
<title>Tolvan Crest — Business Card</title>
<link rel="stylesheet" href="https://fonts.googleapis.com/css2?family=Open+Sans:wght@400;600;800&display=swap">
<style>
  :root {
    --ink: #111111;
    --charcoal: #3b3b3b;
    --accent: #f5930f;
    --band: #444444;
    --band-text: #f2f2f2;
    --paper-light: #ffffff;
    --paper-edge: #e4e4e4;
  }
  * { margin: 0; padding: 0; box-sizing: border-box; }
  html, body { width: 1200px; height: 741px; overflow: hidden; }
  body { font-family: "Open Sans", Arial, sans-serif; }
  .card {
    position: relative;
    width: 1200px;
    height: 741px;
    background: radial-gradient(ellipse at 45% 45%, var(--paper-light) 40%, var(--paper-edge) 100%);
    overflow: hidden;
  }
  .contact {
    position: absolute;
    top: 36px;
    left: 690px;
    width: 490px;
    text-align: center;
    color: var(--ink);
  }
  .contact-name {
    font-weight: 800;
    font-size: 66px;
    line-height: 1.05;
    letter-spacing: -0.5px;
  }
  .contact-title {
    font-weight: 400;
    font-size: 29px;
    line-height: 1.1;
    letter-spacing: -0.5px;
  }
  .contact-line {
    font-weight: 400;
    font-size: 28px;
    line-height: 1.25;
  }
  .contact-line strong { font-weight: 600; }
  .brand {
    position: absolute;
    top: 330px;
    left: 0;
    width: 1200px;
    display: flex;
    align-items: center;
    justify-content: center;
    gap: 28px;
  }
  .brand-dot {
    width: 70px;
    height: 70px;
    border-radius: 50%;
    background: var(--accent);
    flex: none;
  }
  .brand-name {
    font-weight: 600;
    font-size: 104px;
    line-height: 1;
    color: var(--charcoal);
    letter-spacing: -1px;
  }
  .address-band {
    position: absolute;
    left: 0;
    bottom: 0;
    width: 1200px;
    height: 55px;
    background: var(--band);
    display: flex;
    align-items: center;
    justify-content: center;
    gap: 14px;
    color: var(--band-text);
    font-size: 26px;
  }
  .address-band svg { width: 14px; height: 22px; flex: none; }
</style>
</head>
<body>
  <main class="card">
    <section class="contact">
      <h1 class="contact-name">REED HALVORSEN</h1>
      <p class="contact-title">MANUFACTURERS REP PRINCIPAL</p>
      <p class="contact-line">Cell : <strong>904-555-0162</strong></p>
      <p class="contact-line">rhalvorsen@tolvanmail.com</p>
    </section>

    <div class="brand">
      <span class="brand-dot"></span>
      <span class="brand-name">Tolvan Crest</span>
    </div>

    <footer class="address-band">
      <svg viewBox="0 0 14 22" aria-hidden="true"><path d="M11 2 L3 11 L11 20" fill="none" stroke="currentColor" stroke-width="3.5"/></svg>
      <span class="address-text">1470 Harbor Lane South ,Marlow Beach, FL 32961</span>
      <svg viewBox="0 0 14 22" aria-hidden="true"><path d="M3 2 L11 11 L3 20" fill="none" stroke="currentColor" stroke-width="3.5"/></svg>
    </footer>
  </main>
</body>
</html>
```